Business card for Velvet & Lark weddings and events management company
Velvet & Lark
Business card for Velvet & Lark weddings and events management company - Events
Creative Brief
Modern
Nargiza Huseynova
General Manager
17 Samad Str. AZ 1014, Baku, Azerbaijan
nargiza.huseynova@velvetlark-example.az
www.velvetlark-example.az
In addition to english version, be ready to provide azerbaijani version with little changes in titles as seen below: Name: Nərgizə Hüseynova Title: Müdir Address: Samad küç., 17 AZ1014, Bakı, Azərbaycan Slogan on the back: Sevindirməklə sevinirik! (as seen on azerbaijani version of logo, using only capital letters)
HAPPY TO MAKE YOU HAPPY! SEVİNDİRMƏKLƏ SEVİNİRİK! (on azerbaijani version) for this option, you can provide a different font as well, something maybe handwritten and more friendly. (Original font is Trajan Pro)
tulipwanderer tulipwanderer

```html
<!DOCTYPE html>
<html lang="en">
<head>
<meta charset="utf-8">
<title>Velvet &amp; Lark — Business Card</title>
<link rel="stylesheet" href="https://fonts.googleapis.com/css2?family=Cinzel:wght@400&family=Open+Sans:wght@400;700&display=swap">
<style>
  :root {
    --page-bg: #e9e9ea;
    --card-white: #ffffff;
    --frame-black: #0d0d0d;
    --frame-grey: #9a9a9a;
    --brand-grey: #5c5c5e;
    --ink: #1c1c1c;
    --ink-soft: #3a3a3a;
  }
  * { margin: 0; padding: 0; box-sizing: border-box; }
  html, body {
    width: 1200px;
    height: 900px;
    overflow: hidden;
    background: var(--page-bg);
  }
  .canvas {
    position: relative;
    width: 1200px;
    height: 900px;
  }
  .card {
    position: absolute;
    left: 120px;
    top: 180px;
    width: 960px;
    height: 540px;
    border-radius: 270px;
    background: var(--card-white);
    border: 26px solid var(--frame-black);
  }
  .card__inner-rule {
    position: absolute;
    inset: 14px;
    border-radius: 256px;
    border: 4px solid var(--frame-grey);
  }
  .brand {
    position: absolute;
    left: 0;
    right: 0;
    top: 118px;
    display: flex;
    align-items: center;
    justify-content: center;
    gap: 18px;
  }
  .brand__dot {
    width: 30px;
    height: 30px;
    border-radius: 50%;
    background: var(--brand-grey);
  }
  .brand__name {
    font-family: "Cinzel", serif;
    font-weight: 400;
    font-size: 46px;
    letter-spacing: 2px;
    color: var(--brand-grey);
  }
  .person {
    position: absolute;
    left: 0;
    right: 0;
    top: 206px;
    text-align: center;
    font-family: "Open Sans", sans-serif;
    color: var(--ink);
  }
  .person__name {
    font-weight: 700;
    font-size: 34px;
    letter-spacing: 0.5px;
    text-transform: uppercase;
  }
  .person__title {
    font-weight: 400;
    font-size: 22px;
    color: var(--ink-soft);
    margin-top: 2px;
  }
  .contact {
    position: absolute;
    right: 120px;
    top: 318px;
    text-align: right;
    font-family: "Open Sans", sans-serif;
    font-size: 19px;
    line-height: 30px;
    color: var(--ink-soft);
  }
  .contact__line {
    display: flex;
    align-items: center;
    justify-content: flex-end;
    gap: 8px;
    white-space: nowrap;
  }
  .contact__icon {
    width: 16px;
    height: 18px;
    flex: none;
    fill: var(--ink);
  }
</style>
</head>
<body>
  <div class="canvas">
    <div class="card">
      <div class="card__inner-rule"></div>

      <div class="brand">
        <span class="brand__dot"></span>
        <span class="brand__name">VELVET &amp; LARK</span>
      </div>

      <div class="person">
        <div class="person__name">Nargiza Huseynova</div>
        <div class="person__title">General Manager</div>
      </div>

      <div class="contact">
        <div class="contact__line">nargiza.huseynova@velvetlark-example.az</div>
        <div class="contact__line">
          <svg class="contact__icon" viewBox="0 0 16 18" aria-hidden="true">
            <path d="M8 0a6 6 0 0 0-6 6c0 4.5 6 12 6 12s6-7.5 6-12a6 6 0 0 0-6-6zm0 8.5A2.5 2.5 0 1 1 8 3.5a2.5 2.5 0 0 1 0 5z"/>
          </svg>
          17 Samad Str. AZ 1014, Baku, Azerbaijan
        </div>
        <div class="contact__line">
          <svg class="contact__icon" viewBox="0 0 16 18" aria-hidden="true">
            <path d="M3.5 1.5l2.6 3.2-1.6 1.6c.9 2 2.5 3.7 4.6 4.8l1.6-1.6 3.3 2.5-1.4 2.9C7.3 14.6 2 9.3 1 3z"/>
          </svg>
          012 555 0148 @ www.velvetlark-example.az
        </div>
      </div>
    </div>
  </div>
</body>
</html>
```